hawkforge structural steel

8 1/2" x 11" flyer color both sides. Use at least 12 pictures.

Add the word; structural under HawkForge to logo

bullet points:
Laser Accuracy
On-time scheduling
Own our Equipment
39 Years Exp.
Manufacturing Construction Brackets Since 1982
We manufacture custom ibeams in Phoenix, AZ
Certified welders

Hawkforge Plant
2814 n. 17th avenue, suite-3
Phx, AZ 85019
480-629-8107

Target Market(s)

Architects, builders

Industry/Entity Type

construction

Colors
0054AA
0677BA
7BADD7
CADEEF
E8F1F8

```html
<!DOCTYPE html>
<html lang="en">
<head>
<meta charset="utf-8">
<title>HawkForge Structural – Flyer</title>
<link rel="stylesheet" href="https://fonts.googleapis.com/css2?family=Montserrat:wght@500;600;700;800&display=swap">
<style>
  :root {
    --page-bg: #f2f2f4;
    --panel-blue: #44618a;
    --brand-red: #dc2528;
    --steel-dark: #5f7699;
    --steel-mid: #8ea2c2;
    --steel-light: #b8c6dc;
    --white: #ffffff;
  }
  * { margin: 0; padding: 0; box-sizing: border-box; }
  html, body {
    width: 1200px; height: 1000px; overflow: hidden;
    background: var(--page-bg);
    font-family: "Montserrat", Arial, sans-serif;
  }
  .flyer {
    position: absolute; left: 357px; top: 185px;
    width: 485px; height: 628px;
    background: var(--panel-blue);
    overflow: hidden;
    color: var(--white);
  }
  .steel-photo {
    position: absolute; left: 191px; top: 0; width: 294px; height: 440px;
    background:
      repeating-linear-gradient(90deg, rgba(255,255,255,0.18) 0 6px, rgba(40,60,95,0.25) 6px 14px, rgba(255,255,255,0.08) 14px 26px),
      linear-gradient(180deg, var(--steel-light), var(--steel-mid) 55%, var(--steel-dark));
  }
  .red-field { position: absolute; left: 0; top: 0; width: 485px; height: 628px; }
  .experience-band {
    position: absolute; left: 191px; top: 28px; width: 294px; height: 27px;
    background: rgba(220,37,40,0.88);
    font-size: 11.5px; font-weight: 700; letter-spacing: 2.2px;
    display: flex; align-items: center; justify-content: center;
  }
  .brand {
    position: absolute; text-align: center; font-weight: 700; line-height: 1;
  }
  .brand-mark {
    display: block; width: 14px; height: 14px; border-radius: 50%;
    background: var(--white); margin: 0 auto 8px;
  }
  .brand-name { display: block; letter-spacing: 0.5px; }
  .brand-sub { display: block; letter-spacing: 4px; }
  .brand--top { left: 22px; top: 30px; width: 120px; }
  .brand--top .brand-name { font-size: 17px; }
  .brand--top .brand-sub { font-size: 7px; margin-top: 3px; letter-spacing: 3.4px; }
  .brand--bottom { left: 331px; top: 450px; width: 146px; }
  .brand--bottom .brand-mark { width: 18px; height: 18px; }
  .brand--bottom .brand-name { font-size: 21px; }
  .brand--bottom .brand-sub { font-size: 8px; margin-top: 3px; letter-spacing: 4.4px; }
  .tagline {
    position: absolute; left: 24px; top: 99px;
    font-size: 10.6px; font-weight: 600; letter-spacing: 2.4px; white-space: nowrap;
  }
  .tagline-rule {
    position: absolute; left: 24px; top: 114px; width: 33px; height: 3px;
    background: var(--brand-red);
  }
  .features { position: absolute; left: 24px; top: 171px; list-style: none; }
  .features li {
    display: flex; align-items: center; height: 38px;
    font-size: 13.4px; font-weight: 700; white-space: nowrap;
    text-shadow: 0 0 3px rgba(40,60,95,0.5);
  }
  .features li::before {
    content: ""; width: 7px; height: 7px; background: var(--brand-red); margin-right: 8px;
  }
  .weld-photo {
    position: absolute; left: 24px; top: 397px; width: 173px; height: 173px;
    border-radius: 50%; border: 3px solid var(--white);
    background: radial-gradient(circle at 38% 62%, #e6f0ff 0 6%, #5a8fe0 18%, #1d3f86 45%, #1a1f33 75%, #4a3a2a 100%);
  }
  .plant-address {
    position: absolute; right: 16px; top: 570px; text-align: right;
    font-size: 8.6px; font-weight: 700; line-height: 11px;
  }
</style>
</head>
<body>
  <main class="flyer">
    <div class="steel-photo" role="img" aria-label="Close-up photo of vertical steel rebar rods"></div>
    <svg class="red-field" viewBox="0 0 485 628" aria-hidden="true">
      <polygon points="0,628 191,345 485,420 485,628" fill="var(--brand-red)"/>
    </svg>

    <div class="experience-band">39 YEARS OF EXPERIENCE</div>

    <div class="brand brand--top">
      <span class="brand-mark"></span>
      <span class="brand-name">HAWKFORGE</span>
      <span class="brand-sub">STRUCTURAL</span>
    </div>

    <p class="tagline">MANUFACTURING CONSTRUCTION BRACKETS SINCE 1982</p>
    <div class="tagline-rule"></div>

    <ul class="features">
      <li>LASER ACCURACY</li>
      <li>ON TIME SCHEDULING</li>
      <li>OWN OUR EQUIPMENT</li>
      <li>WE MANUFACTURE CUSTOM IBEAMS IN PHOENIX, AZ</li>
      <li>CERTIFIED WELDERS</li>
    </ul>

    <div class="weld-photo" role="img" aria-label="Photo of a welder at work with blue sparks"></div>

    <div class="brand brand--bottom">
      <span class="brand-mark"></span>
      <span class="brand-name">HAWKFORGE</span>
      <span class="brand-sub">STRUCTURAL</span>
    </div>

    <address class="plant-address" style="font-style:normal">
      HAWKFORGE PLANT<br>
      2814 N. 17TH AVENUE, SUITE-3<br>
      PHX, AZ 85019<br>
      480-629-8107
    </address>
  </main>
</body>
</html>
```